I want to revise my business card design and get a more modern and up to date design.

Brolvane Handyman Sevices originated from a family-owned and operated contractor business, performing home renovation, addition, and construction work in the NYC area since 2004. Today, we specialize in reliable and affordable handyman services for residential and commercial clients In 2014, we expanded to northern New Jersey. In 2016, we brought quality home improvement and repair services to new Bucks County, PA, and nearby New Jersey areas.
Target Market(s)
Home owners and business that might be looking for a General contractor, handyman, cleaning services and Home maintenance and property.
Industry/Entity Type
Construction Company
Contact Information for Business Card
I am open to new ideas
Colors
Designer to choose colors to be used in the design.
Look and feel
Each slider illustrates characteristics of the customer's brand and the style your logo design should communicate.

```html
<!DOCTYPE html>
<html lang="en">
<head>
<meta charset="utf-8">
<title>Brolvane Handyman Sevices – Business Card</title>
<link rel="stylesheet" href="https://fonts.googleapis.com/css2?family=Work+Sans:wght@400;500;700;800&display=swap">
<style>
  :root {
    --stage: #141414;
    --card: #232323;
    --card-edge: #2c2c2c;
    --red: #e8202a;
    --white: #ffffff;
    --grey: #8a8a8a;
  }
  * { box-sizing: border-box; margin: 0; padding: 0; }
  html, body {
    width: 1200px; height: 900px; overflow: hidden;
    background: var(--stage);
    font-family: "Work Sans", Arial, sans-serif;
  }
  .stage { position: relative; width: 1200px; height: 900px; }
  .card {
    position: absolute; left: 240px; width: 720px; height: 400px;
    background: var(--card);
    border: 1px solid var(--card-edge);
    box-shadow: 0 14px 30px rgba(0,0,0,.55);
  }
  .card--front { top: 35px; }
  .card--back { top: 465px; }

  .brand { position: absolute; display: flex; flex-direction: column; }
  .brand__row { display: flex; align-items: center; gap: 14px; }
  .brand__dot {
    width: 22px; height: 22px; border-radius: 50%;
    background: var(--red); flex: none;
  }
  .brand__name {
    color: var(--white); font-weight: 800; letter-spacing: -1px; line-height: 1;
  }
  .brand__tag {
    color: var(--grey); text-transform: uppercase; font-weight: 500;
    letter-spacing: 5px; margin-top: 8px;
  }
  .card--front .brand { left: 50%; top: 50%; transform: translate(-50%, -50%); }
  .card--front .brand__name { font-size: 72px; }
  .card--front .brand__tag { font-size: 14px; padding-left: 36px; }

  .card--back .brand { left: 56px; top: 160px; }
  .card--back .brand__name { font-size: 56px; }
  .card--back .brand__tag { font-size: 12px; letter-spacing: 4px; padding-left: 36px; }

  .divider {
    position: absolute; left: 380px; top: 70px; width: 2px; height: 260px;
    background: var(--red);
  }
  .contact { position: absolute; left: 418px; top: 82px; color: var(--white); }
  .contact__name {
    color: var(--red); font-weight: 700; font-size: 24px;
    text-transform: uppercase; letter-spacing: .5px;
  }
  .contact__role { font-size: 18px; margin-top: 2px; }
  .contact__address { font-size: 18px; line-height: 1.35; margin-top: 16px; }
  .contact__list { list-style: none; margin-top: 14px; font-size: 18px; line-height: 1.6; }
  .contact__list li { display: flex; align-items: center; gap: 10px; }
  .contact__list svg { width: 13px; height: 13px; flex: none; }
</style>
</head>
<body>
<main class="stage">
  <section class="card card--front">
    <div class="brand">
      <div class="brand__row">
        <span class="brand__dot"></span>
        <span class="brand__name">Brolvane</span>
      </div>
      <span class="brand__tag">Handyman Services</span>
    </div>
  </section>

  <section class="card card--back">
    <div class="brand">
      <div class="brand__row">
        <span class="brand__dot"></span>
        <span class="brand__name">Brolvane</span>
      </div>
      <span class="brand__tag">Handyman Services</span>
    </div>

    <div class="divider"></div>

    <div class="contact">
      <p class="contact__name">Darren Kolby</p>
      <p class="contact__role">Director</p>
      <p class="contact__address">218b Harlow Street,<br>Lindmere, NZ, 4102</p>
      <ul class="contact__list">
        <li>
          <svg viewBox="0 0 16 16" aria-hidden="true"><path d="M4 1l3 3-2 2c1 2 3 4 5 5l2-2 3 3-2 3C7 15 1 9 1 3z" fill="none" stroke="#e8202a" stroke-width="1.6"/></svg>
          (555) 014-2290
        </li>
        <li>
          <svg viewBox="0 0 16 16" aria-hidden="true"><rect x="1.5" y="3.5" width="13" height="9" fill="none" stroke="#e8202a" stroke-width="1.5"/><path d="M1.5 3.5l6.5 5 6.5-5" fill="none" stroke="#e8202a" stroke-width="1.5"/></svg>
          info@brolvanefix.com
        </li>
        <li>
          <svg viewBox="0 0 16 16" aria-hidden="true"><circle cx="8" cy="8" r="6.5" fill="none" stroke="#e8202a" stroke-width="1.4"/><ellipse cx="8" cy="8" rx="3" ry="6.5" fill="none" stroke="#e8202a" stroke-width="1.2"/><path d="M1.5 8h13" stroke="#e8202a" stroke-width="1.2"/></svg>
          www.brolvanefix.com
        </li>
      </ul>
    </div>
  </section>
</main>
</body>
</html>
```